Modern Can & Tray Design Competition

Please note our brand is now called zé, please do not submit any entries with the wording or logo of "zé kelpwater". Read the full design brief below before making an entry, please.

A competition to design can packaging and outer tray designs for a new exciting brand.

See examples of the design assets I want, below, including both a can and outer tray:

1. https://quillmarketgoods.eu/beverages/energy-drinks/vomba-boost-the-amber-edition-12-x-025-liter-cans-nl/?lang=en

2. https://www.plimvo.com/nl/nl/p/tarvo-fizz-cherry-slim-cans-24-x-330-ml-eu/4812000077312904/

We have 2 flavours in our range, so we need two separate can designs and a separate outer tray design for each flavour.

Our drinks are currently packaged in PET plastic bottles. Our flavours are:
Lemon & Lime - https://zekelpwater.co.uk/products/lemon-and-lime
Strawberry - https://zekelpwater.co.uk/products/strawberry

For this competition, I want can designs for each flavour in 250ml style cans like used by Vomba. And I also want an outer tray for the cans designed for each flavour. Our brand is changing to “zé” so please do not use “kelpwater” on any part of the design. The logo should be “zé” and for each flavour the ze should show the fruit for the flavour embedded inside it. See the files called “ze_fruit_logo_LEMLI (1)” and “ze_fruit_logo_STR (1)” for what I mean. You can use these files for your design.

Under the logo it should state on the can “Prebiotic Fibre Drink”. Similar to how VomBa has “Energy Drink” written under its logo: https://www.drenvilo.com/wp-content/uploads/2009/11/vomba-can-250ml-1.jpg

If you can submit your design ideas for this competition with a picture of the can next to the tray like this for each flavour, that will be best: https://img.keltoshop.com/images/I/57qTzWa2pLx._SL1500_.jpg

So, two design concepts/ideas are needed to enter: One for Lemon & Lime and one for Strawberry.

We want vibrant, eye-catching packaging designs that will catch the consumer's attention.

Right now, we have ze in the centre of our packaging design with fruit embedded in the ze. This must remain a key part of your design as mentioned above. Also, as we will be launching other drinks as a company under different brand names and to unify our different brands we want a splash effect on all the cans which will be replicated across our other brands. So, please have some kind of splash effect on each flavour that can be replicated on the cans of our other brands in future.

Design considerations:

There is also certain information we need on the front/face of the can.

On the very top of the can just below the neck and above the logo we want it to state: “Supports Gut & Overall health*” example: https://pmkgrocerhub.co.uk/wp-content/uploads/2023/10/Brova-Zest-Lemonade.jpg

We also want the number of calories to be stated somewhere on the can in a clever way like in a droplet of the water splash effect. The number of the calories is “17 kcals”.

Under the ze logo as mentioned we want the wording: “Prebiotic Fibre Drink”

Then under Prebiotic Fibre Drink we want the name of the flavour - and then under the flavour we want 3 features stated. Which are:

“20% of daily fibre”
“0g sugar”
“Nothing artificial“

This could be laid out as 3 circles with icons or some other way. The last piece of information under these 3 features is then the size of the can “250 mle”.

In terms of “feel” of the design we want a vibrant colourful feel, and it should show pictures of fruit on it. Here is an example
https://gardenhollowtonics.com/wp-content/uploads/sites/2/2023/03/GHT-US-SodaRange-%E2%80%93-bb-1220x883.png

Any questions let me know. I look forward to seeing your ideas.

To see more about our brand, view our website: www.zekelpwater.co.uk

```html
<!DOCTYPE html>
<html lang="en">
<head>
<meta charset="utf-8">
<title>zé Prebiotic Fibre Drink – Lemon &amp; Lime Can</title>
<link rel="stylesheet" href="https://fonts.googleapis.com/css2?family=Outfit:wght@500;700&family=Arvo:wght@700&display=swap">
<style>
  :root {
    --page-bg: #efefef;
    --can-light: #e3e6ae;
    --can-mid: #d3d98e;
    --can-deep: #bcc46a;
    --band: #d3da7c;
    --pattern-strong: rgba(222, 214, 70, 0.55);
    --pattern-soft: rgba(230, 224, 110, 0.25);
    --splash-lemon: #e4dc6a;
    --splash-lime: #8db556;
    --splash-leaf: #4f7f48;
    --splash-water: #92d2d2;
    --leaf-green: #3f6b2f;
    --title-grey: #3b3b3b;
    --logo-tile: #ececec;
    --rim: #d9d9d9;
  }
  * { box-sizing: border-box; margin: 0; padding: 0; }
  html, body { width: 1200px; height: 800px; overflow: hidden; }
  body { background: var(--page-bg); position: relative; font-family: "Outfit", sans-serif; }

  .can {
    position: absolute; left: 510px; top: 160px; width: 208px; height: 516px;
    background: linear-gradient(90deg, var(--can-deep) 0%, var(--can-mid) 12%, var(--can-light) 45%, var(--can-mid) 80%, var(--can-deep) 100%);
    border-top: 6px solid var(--rim);
    border-bottom: 8px solid var(--rim);
    overflow: hidden;
  }
  .claim-band {
    position: absolute; left: 0; top: 6px; width: 100%; height: 29px;
    background: var(--band);
    display: flex; align-items: center; justify-content: center;
    font-size: 10.5px; font-weight: 500; color: var(--leaf-green);
  }
  .fruit-pattern {
    position: absolute; left: 0; top: 35px; width: 100%; height: 150px;
    background:
      radial-gradient(circle at 22% 20%, var(--pattern-strong) 0 14%, transparent 26%),
      radial-gradient(circle at 60% 15%, var(--pattern-strong) 0 16%, transparent 28%),
      radial-gradient(circle at 85% 35%, var(--pattern-strong) 0 12%, transparent 24%),
      radial-gradient(circle at 40% 55%, var(--pattern-strong) 0 12%, transparent 24%),
      radial-gradient(circle at 12% 80%, var(--pattern-strong) 0 14%, transparent 26%),
      radial-gradient(circle at 80% 85%, var(--pattern-strong) 0 12%, transparent 24%),
      linear-gradient(180deg, var(--pattern-soft), rgba(230,224,110,0.15));
  }
  .splash {
    position: absolute; left: 18px; top: 128px; width: 172px; height: 172px; border-radius: 50%;
    background:
      radial-gradient(circle at 32% 38%, var(--splash-lemon) 0 22%, transparent 34%),
      radial-gradient(circle at 70% 30%, var(--splash-leaf) 0 12%, transparent 24%),
      radial-gradient(circle at 40% 78%, var(--splash-leaf) 0 14%, transparent 26%),
      radial-gradient(circle at 68% 70%, var(--splash-lime) 0 20%, transparent 32%),
      radial-gradient(circle at 50% 50%, var(--splash-lemon) 0 40%, var(--splash-lime) 62%, var(--splash-water) 82%, rgba(146,210,210,0) 100%);
  }
  .logo-tile {
    position: absolute; left: 71px; top: 183px; width: 65px; height: 67px;
    background: var(--logo-tile); border-radius: 6px;
    display: flex; align-items: center; justify-content: center;
    font-size: 34px; font-weight: 700; color: var(--leaf-green);
  }
  .kcal-drop { position: absolute; left: 132px; top: 255px; width: 24px; height: 32px; }
  .product-title {
    position: absolute; left: 0; top: 295px; width: 100%; text-align: center;
    font-size: 24px; line-height: 24px; font-weight: 700; color: var(--title-grey);
  }
  .flavour {
    position: absolute; left: 0; top: 351px; width: 100%; text-align: center;
    font-family: "Arvo", serif; font-weight: 700; font-size: 10px; color: var(--leaf-green);
  }
  .features {
    position: absolute; left: 0; top: 404px; width: 100%;
    display: flex; justify-content: center; gap: 12px;
  }
  .feature {
    width: 30px; height: 30px; border: 1px solid var(--leaf-green); border-radius: 3px;
    display: flex; flex-direction: column; align-items: center; justify-content: center;
    font-size: 4px; line-height: 4.5px; color: var(--leaf-green); text-align: center; font-weight: 500;
  }
  .feature svg { width: 9px; height: 9px; margin-bottom: 2px; }
  .volume {
    position: absolute; left: 0; top: 474px; width: 100%; text-align: center;
    font-size: 9.5px; font-weight: 700; color: var(--leaf-green);
  }
</style>
</head>
<body>
  <div class="can">
    <div class="fruit-pattern" role="img" aria-label="Line-drawn pattern of lemons, lime slices and leaves"></div>
    <div class="claim-band">Supports Gut &amp; Overall Health</div>
    <div class="splash" role="img" aria-label="Water splash ring around fresh lemons and limes with leaves"></div>
    <div class="logo-tile">zé</div>
    <svg class="kcal-drop" viewBox="0 0 30 40" aria-label="17 kcals">
      <path d="M15 1 C15 1 2 18 2 26 A13 13 0 0 0 28 26 C28 18 15 1 15 1 Z" fill="#3f6b2f"/>
      <text x="15" y="28" text-anchor="middle" font-family="Outfit, sans-serif" font-weight="700" font-size="10" fill="#e3e6ae">17</text>
      <text x="15" y="34" text-anchor="middle" font-family="Outfit, sans-serif" font-size="4.5" fill="#e3e6ae">kcals</text>
    </svg>
    <h1 class="product-title">PREBIOTIC<br>FIBRE DRINK</h1>
    <p class="flavour">Lemon &amp; Lime</p>
    <div class="features">
      <div class="feature">
        <svg viewBox="0 0 10 10"><path d="M5 9 V4 M5 5 C2 5 2 2 2 2 C5 2 5 5 5 5 M5 4 C8 4 8 1 8 1 C5 1 5 4 5 4" stroke="#3f6b2f" fill="none" stroke-width="1"/></svg>
        <span>20% of<br>daily fibre</span>
      </div>
      <div class="feature">
        <svg viewBox="0 0 10 10"><rect x="3" y="0.5" width="4" height="4" fill="#3f6b2f"/><rect x="0.5" y="5" width="4" height="4" fill="#3f6b2f"/><rect x="5.5" y="5" width="4" height="4" fill="#3f6b2f"/></svg>
        <span>0g<br>sugar</span>
      </div>
      <div class="feature">
        <svg viewBox="0 0 10 10"><path d="M3 0 C7 3 3 7 7 10 M7 0 C3 3 7 7 3 10" stroke="#3f6b2f" fill="none" stroke-width="1"/></svg>
        <span>Nothing<br>artificial</span>
      </div>
    </div>
    <p class="volume">8.5 fl. oz. (250ml)</p>
  </div>
</body>
</html>
```